Namecard and logo for New startup cloud communication company

We need name card and logo deign for our company

company name Bex Tamarind Pte Ltd
Its a cloud base company offering IP PBX communication solutions
Young start up company base in Singapore with experience in asterisk solutions

We require the design to be unique and updated
to incorporate Bex and Cloud into the design.

Industry/Entity Type

Communication

Contact Information for Business Card

We require the following on name card

Company name
Name
Company address
Mobile Number and main line with ext
email address
website address

Font styles to use
Sans Serif

```html
<!DOCTYPE html>
<html lang="en">
<head>
<meta charset="utf-8">
<title>Bex Tamarind Business Card</title>
<link rel="stylesheet" href="https://fonts.googleapis.com/css2?family=Mulish:wght@400;700&display=swap">
<style>
  :root {
    --page-bg: #e9e7e4;
    --card-white: #ffffff;
    --brand-blue: #2872a8;
    --name-blue: #1f64a0;
    --text-grey: #7c7c7c;
    --logo-grey: #8a8a8a;
    --backdrop-tint: #e7eaf2;
    --shadow: 0 6px 14px rgba(0,0,0,0.35);
  }
  * { margin: 0; padding: 0; box-sizing: border-box; }
  html, body {
    width: 1200px; height: 1000px; overflow: hidden;
    background: var(--page-bg);
    font-family: "Mulish", sans-serif;
  }
  .canvas { position: relative; width: 1200px; height: 1000px; }
  .card {
    position: absolute; left: 265px; width: 665px; height: 397px;
    border-radius: 24px; box-shadow: var(--shadow); overflow: hidden;
  }
  .card-front { top: 73px; background: var(--card-white); }
  .card-back { top: 532px; background: var(--brand-blue); }

  .backdrop-disc {
    position: absolute; left: 60px; top: 95px;
    width: 360px; height: 360px; border-radius: 50%;
    background: var(--backdrop-tint);
  }

  .brand {
    position: absolute; display: flex; flex-direction: column; align-items: center;
    font-weight: 400; white-space: nowrap; line-height: 1;
  }
  .brand-mark { border-radius: 50%; flex: none; }
  .front-brand { right: 38px; top: 42px; gap: 18px; font-size: 44px; color: var(--logo-grey); }
  .front-brand .brand-mark { width: 92px; height: 92px; background: var(--brand-blue); }
  .back-brand { left: 0; right: 0; top: 82px; gap: 50px; font-size: 60px; color: var(--card-white); }
  .back-brand .brand-mark { width: 124px; height: 124px; background: var(--card-white); }

  .holder { position: absolute; left: 40px; top: 202px; }
  .holder-name { font-size: 19px; font-weight: 700; color: var(--name-blue); line-height: 24px; }
  .holder-role { font-size: 17px; color: var(--text-grey); line-height: 22px; }

  .contact-list { position: absolute; left: 40px; top: 273px; list-style: none; }
  .contact-list li {
    display: flex; align-items: center; gap: 8px;
    font-size: 16px; color: var(--text-grey); line-height: 21px;
  }
  .contact-list svg { width: 12px; height: 12px; fill: var(--name-blue); flex: none; }

  .company { position: absolute; right: 38px; top: 291px; text-align: right; }
  .company-name { font-size: 17px; font-weight: 700; color: var(--name-blue); line-height: 22px; }
  .company-address { font-size: 16px; color: var(--text-grey); line-height: 21px; }
</style>
</head>
<body>
<main class="canvas">
  <section class="card card-front">
    <div class="backdrop-disc" aria-hidden="true"></div>

    <div class="brand front-brand"><span class="brand-mark"></span>Bex Tamarind</div>

    <div class="holder">
      <p class="holder-name">Dana Whitlow</p>
      <p class="holder-role">Founder / CEO</p>
    </div>

    <ul class="contact-list">
      <li>
        <svg viewBox="0 0 12 12" aria-hidden="true"><path d="M3 0h6a1 1 0 0 1 1 1v10a1 1 0 0 1-1 1H3a1 1 0 0 1-1-1V1a1 1 0 0 1 1-1zm0.5 1.5v8h5v-8z"/></svg>
        + 999 999 9999
      </li>
      <li>
        <svg viewBox="0 0 12 12" aria-hidden="true"><path d="M0 3.5C1.5 1.5 10.5 1.5 12 3.5L11 5 8.5 4.5V3.5h-5v1L1 5zM2.5 6h7l1.5 5H1z"/></svg>
        + 999 999 9999
      </li>
      <li>
        <svg viewBox="0 0 12 12" aria-hidden="true"><path d="M0 2h12v8H0zm1 1v.6l5 3.2 5-3.2V3z"/></svg>
        info@bextamarind.com
      </li>
      <li>
        <svg viewBox="0 0 12 12" aria-hidden="true"><path d="M5 7l2-2 .8.8-2 2zM3.2 6.6l1 1-1.4 1.4a.9.9 0 0 0 1.3 1.3l1.4-1.4 1 1-1.4 1.4A2.3 2.3 0 0 1 1.8 8zM8.8 5.4l-1-1 1.4-1.4a.9.9 0 0 0-1.3-1.3L6.5 3.1l-1-1L6.9.7A2.3 2.3 0 0 1 10.2 4z"/></svg>
        www.bextamarind.com
      </li>
    </ul>

    <div class="company">
      <p class="company-name">Bex Tamarind Pte Ltd</p>
      <p class="company-address">14 Calloway Lane</p>
      <p class="company-address">Riverton VIC 3921</p>
    </div>
  </section>

  <section class="card card-back">
    <div class="brand back-brand"><span class="brand-mark"></span>Bex Tamarind</div>
  </section>
</main>
</body>
</html>
```